BrookVale Collision Repair Web Site

Create a web site that will inform my potential customers about the services I provide. We are a Automotive Collision repair business that uses the latest state of the art equipment, computerized paint matching highly trained technicians, have over 30 years experience. We work with all all insurance programs. Our Moto is "Fixed Right, The First Time, Every Time". BrookVale, The trusted pick in collision repair.

Target Market(s)

People that have been in a auto collision, needs windshield replaced, people that drive 10 year or newer cars

Industry/Entity Type

Automotive

Coding

Coded - Design and coding required

Number of Pages Required

4 page

Font styles to use
Sans Serif

Requirements
Must have
• Logo, Place for Phone number, I need to be able to put the code in so I can use a tracking phone number
• site needs to be mobile ready or adaptive
• May want to have a photo of a high end car
• here is a web site for example with the pages that I want
• https://www.pondlyautobody.example/online-repair-estimate,
• https://www.pondlyautobody.example/schedule-appointment
• https://www.pondlyautobody.example/collision-repair/auto-body-repair
• https://www.pondlyautobody.example/contact
Nice to have
• Be great if the Car in the log could have the front damaged then have it fix in a animation. Not sure if could be done here

```html
<!DOCTYPE html>
<html lang="en">
<head>
<meta charset="utf-8">
<title>BrookVale Collision Repair</title>
<link href="https://fonts.googleapis.com/css2?family=Montserrat:wght@400;500;600;700;800&family=Lato:wght@300;400;700&display=swap" rel="stylesheet">
<style>
:root{
  --blue:#0e4fa4;
  --blue-dark:#0a3f86;
  --green:#8cc63f;
  --ink:#333638;
  --muted:#66696c;
  --light:#f7f7f7;
  --rule:#cfd2d5;
  --footer:#3c3e41;
  --white:#ffffff;
}
*{margin:0;padding:0;box-sizing:border-box}
html,body{width:1200px;height:3140px;overflow:hidden}
body{position:relative;font-family:"Lato",sans-serif;color:var(--ink);background:var(--white)}
.abs{position:absolute}
a{color:inherit}
.head{font-family:"Montserrat",sans-serif}

/* hero */
.hero{left:0;top:0;width:1200px;height:560px;background:linear-gradient(115deg,#2c3034 0%,#4a4f54 40%,#6d7075 62%,#3a3d41 100%)}
.brand{left:156px;top:38px;color:var(--white);font-family:"Montserrat",sans-serif;font-weight:500;font-size:27px;letter-spacing:1px;display:flex;align-items:center;gap:10px}
.brand .dot{width:12px;height:12px;border-radius:50%;background:var(--white)}
.brand-sub{left:156px;top:70px;color:var(--white);font-family:"Montserrat",sans-serif;font-size:11px;letter-spacing:2px}
.toplinks{right:155px;top:30px;color:#d7d9db;font-size:17px;display:flex;gap:10px;align-items:center;font-family:"Lato",sans-serif}
.toplinks u{text-underline-offset:3px}
.toplinks svg{vertical-align:-2px;margin-right:4px}
.nav{left:428px;top:70px;display:flex;font-family:"Montserrat",sans-serif;font-weight:600;font-size:11px;letter-spacing:1px;color:var(--white)}
.nav span{margin-right:56px}
.nav .active{color:var(--green)}
.hero-title{left:0;width:1200px;top:222px;text-align:center;color:var(--white);font-family:"Montserrat",sans-serif;font-weight:600;font-size:31px}
.hero-sub{left:0;width:1200px;top:262px;text-align:center;color:var(--white);font-size:19px;line-height:30px}
.btn{height:28px;display:flex;align-items:center;justify-content:center;font-family:"Montserrat",sans-serif;font-weight:600;font-size:11px;letter-spacing:1px}
.btn-green{background:var(--green);color:var(--ink)}
.btn-blue{background:var(--blue);color:var(--white)}
.reviews-link{left:0;width:1200px;top:406px;text-align:center;color:var(--white);font-style:italic;font-size:15px}

/* repair intro */
.intro{left:0;top:560px;width:1200px;height:480px;background:var(--light)}
.kicker{left:0;width:1200px;top:602px;text-align:center;color:var(--blue);font-family:"Montserrat",sans-serif;font-weight:700;font-size:20px;letter-spacing:.5px}
.mega{left:0;width:1200px;top:624px;text-align:center;color:var(--blue);font-family:"Montserrat",sans-serif;font-weight:800;font-size:58px;letter-spacing:1px}
.rule{height:1px;background:var(--rule)}
.notch{width:18px;height:18px;border-right:1px solid var(--rule);border-bottom:1px solid var(--rule);transform:rotate(45deg)}
.lead{left:0;width:1200px;text-align:center;color:#444;font-size:19px;line-height:24px}

.tiles{left:156px;top:816px;width:888px;height:224px;display:flex}
.tile{width:178px;height:224px;position:relative;color:var(--white);text-align:center;display:flex;flex-direction:column;justify-content:center}
.tile b{font-family:"Montserrat",sans-serif;font-weight:500;font-size:19px}
.tile i{font-style:normal;font-family:"Montserrat",sans-serif;font-size:14px}
.tile .more{position:absolute;left:0;bottom:0;width:178px;height:32px;background:var(--green);color:var(--ink);font-family:"Montserrat",sans-serif;font-size:10px;font-weight:600;letter-spacing:.5px;display:flex;align-items:center;justify-content:center}
.chev{width:26px;height:26px;display:flex;align-items:center;justify-content:center}
.chev-solid{background:var(--blue)}
.chev-line{border:1px solid var(--blue);background:var(--white)}

/* process */
.sec-title{left:0;width:1200px;text-align:center;color:var(--blue);font-family:"Montserrat",sans-serif;font-weight:700;font-size:30px}
.step{width:152px;height:152px;border-radius:50%;border:2px solid var(--blue);overflow:hidden;background:linear-gradient(var(--white) 0 57%,var(--blue) 57% 100%);color:var(--white);font-family:"Montserrat",sans-serif;font-size:12px;font-weight:500;text-align:center}
.step.on{background:linear-gradient(var(--blue) 0 57%,var(--white) 57% 100%);color:var(--blue);box-shadow:0 8px 14px rgba(0,0,0,.2)}
.step svg{display:block;margin:44px auto 0}
.step span{display:block;margin-top:10px}
.step-head{left:232px;top:1392px;font-family:"Montserrat",sans-serif;font-weight:500;font-size:20px;color:var(--ink)}
.step-text{left:232px;top:1428px;width:730px;font-size:13px;line-height:18px;color:var(--muted);font-weight:300}
.learn{left:232px;top:1526px;font-size:13px;font-style:italic;color:var(--green);text-decoration:underline}

/* features */
.features-photo{left:0;top:1593px;width:460px;height:491px;background:linear-gradient(135deg,#c98f6a 0%,#8b6a5c 30%,#2f4f8f 60%,#1c3c7a 100%)}
.features-bg{left:460px;top:1593px;width:740px;height:491px;background:linear-gradient(90deg,#e6e8ea 0%,#f4f5f6 35%,#fbfbfb 100%)}
.menu{left:156px;top:1625px;width:304px}
.menu-row{height:54px;background:var(--green);display:flex;align-items:center;border-bottom:2px solid #7eb535;font-family:"Montserrat",sans-serif;font-weight:500;font-size:14px;color:var(--ink)}
.menu-row .ic{width:76px;display:flex;justify-content:center;border-right:1px solid rgba(255,255,255,.45);height:100%;align-items:center}
.menu-row .lbl{padding-left:16px}
.menu-row.on{background:#1d1f21;color:var(--white);position:relative}
.menu-row.on::after{content:"";position:absolute;right:-12px;top:15px;border-left:12px solid #1d1f21;border-top:12px solid transparent;border-bottom:12px solid transparent}
.panel-title{left:540px;width:500px;top:1650px;text-align:center;font-family:"Montserrat",sans-serif;font-weight:600;font-size:24px;color:var(--ink)}
.panel-text{left:540px;width:500px;top:1690px;text-align:center;font-size:13px;line-height:17.7px;color:var(--muted);font-weight:300}
.panel-link{left:540px;width:500px;top:1831px;text-align:center;font-size:13px;font-style:italic;text-decoration:underline;color:var(--ink)}
.contact-h{left:540px;width:500px;top:1966px;text-align:center;font-family:"Montserrat",sans-serif;font-weight:600;font-size:19px}
.contact-n{left:540px;width:500px;top:1990px;text-align:center;font-size:31px;color:var(--ink)}

/* testimonials */
.quote-card{width:357px;height:332px}
.quote-dark{left:207px;top:2223px;background:linear-gradient(160deg,#4a4e53 0%,#2d3034 55%,#1f2225 100%)}
.qmark{font-family:"Montserrat",sans-serif;font-weight:800;font-size:34px;color:var(--green);line-height:1}
.qtext{font-size:13.5px;line-height:17.6px;font-weight:300}
.qname{font-family:"Montserrat",sans-serif;font-weight:500;font-size:19px}
.qloc{font-size:11px;line-height:16px}
.submit{left:207px;top:2521px;width:357px;height:34px;background:var(--green);display:flex;align-items:center;justify-content:center;font-family:"Montserrat",sans-serif;font-weight:600;font-size:10px;letter-spacing:1px;color:var(--ink)}

/* offers */
.offers-bg{left:0;top:2604px;width:1200px;height:232px;background:#f3f4f5}
.offers-h{font-family:"Montserrat",sans-serif;font-weight:700;font-size:23px}
.search{left:688px;top:2686px;width:356px;height:36px;border:1px solid var(--rule);background:var(--white);display:flex;align-items:center;padding:0 12px;font-size:14px;color:#a3a6a9;gap:8px}

/* footer */
.footer{left:0;top:2836px;width:1200px;height:304px;background:var(--footer);color:#d4d6d8}
.f-title{font-family:"Montserrat",sans-serif;font-size:16px;color:var(--white)}
.f-list{list-style:none;font-size:12px;line-height:19.4px}
.f-list li::before{content:"•";margin-right:8px;color:#cfd2d5}
.f-list li.on{color:var(--green)}
.f-list li.on::before{color:var(--green)}
.social{display:flex;gap:6px}
.social span{width:24px;height:24px;background:#6a6d71}
.social span.on{background:var(--green)}
</style>
</head>
<body>

<!-- hero -->
<div class="abs hero" role="img" aria-label="Photo of a technician working on a car body in a repair shop"></div>
<div class="abs brand"><span class="dot"></span>BrookVale</div>
<div class="abs brand-sub">— COLLISION REPAIR —</div>
<div class="abs toplinks">
  <span><svg width="11" height="15" viewBox="0 0 11 15"><path d="M5.5 0A5.5 5.5 0 0 0 0 5.5C0 9.6 5.5 15 5.5 15S11 9.6 11 5.5A5.5 5.5 0 0 0 5.5 0zm0 7.6a2 2 0 1 1 0-4 2 2 0 0 1 0 4z" fill="#d7d9db"/></svg><u>Locations</u></span>
  <span>/</span>
  <span><svg width="6" height="14" viewBox="0 0 6 14"><circle cx="3" cy="2" r="2" fill="#d7d9db"/><rect x="1" y="5" width="4" height="9" fill="#d7d9db"/></svg>Repair Status</span>
  <span>/</span>
  <span><svg width="9" height="14" viewBox="0 0 9 14"><rect x="0.8" y="0.8" width="7.4" height="12.4" rx="1.5" fill="none" stroke="#d7d9db" stroke-width="1.6"/></svg>(555) 014 2290</span>
</div>
<div class="abs nav">
  <span class="active">— COMPANY —</span>
  <span>REPAIR SERVICES</span>
  <span>OUR PROCESS</span>
  <span>CAREERS</span>
  <span style="margin-right:0">CONTACT</span>
</div>
<div class="abs hero-title">Trusted Collision Repair. Guaranteed Quality.</div>
<div class="abs hero-sub">Automotive Collision repair &nbsp;I&nbsp; Uses the Latest State of the Art Equipment &nbsp;I&nbsp; Highly Trained Technicians<br>Have Over 30 Years Experience</div>
<div class="abs btn btn-green" style="left:392px;top:360px;width:200px">— GET A FREE ESTIMATE —</div>
<div class="abs btn btn-blue" style="left:608px;top:360px;width:200px">— MAKE APPOINTMENT —</div>
<div class="abs reviews-link"><u>Customer Reviews</u> &nbsp;»</div>

<!-- repair intro -->
<div class="abs intro"></div>
<div class="abs kicker">AUTO BODY &nbsp;/&nbsp; COLLISION &nbsp;/&nbsp; WINDSHIELD</div>
<div class="abs mega">REPAIR</div>
<div class="abs rule" style="left:207px;top:704px;width:785px"></div>
<div class="abs notch" style="left:591px;top:695px;background:var(--light)"></div>
<div class="abs lead" style="top:744px">BrookVale Specialists in Collision<br>Auto Body Repair</div>

<div class="abs tiles">
  <div class="tile" role="img" aria-label="Photo of a dented dark car body" style="background:linear-gradient(160deg,#5a636c,#1f2armed)"></div>
</div>
<div class="abs tiles">
  <div class="tile" role="img" aria-label="Photo of a dented dark car body" style="background:linear-gradient(160deg,#6a737c,#20262c)"><b>Auto Dent</b><i>Removal</i></div>
  <div class="tile" role="img" aria-label="Photo of a technician repairing a red car" style="background:linear-gradient(160deg,#8a8f94,#5a2a2a 70%,#8b1e1e)"><b style="margin-top:-38px">Paintless Dent</b><i>Repair</i><span class="more">— FIND OUT MORE —</span></div>
  <div class="tile" role="img" aria-label="Photo of a cracked windshield" style="background:linear-gradient(160deg,#9aa1a7,#5e666d)"><b>Windshield</b><i>Repairs</i></div>
  <div class="tile" role="img" aria-label="Photo of a bumper being spray painted" style="background:linear-gradient(160deg,#b4bac0,#6e757c)"><b>Bumper</b><i>Repair</i></div>
  <div class="tile" role="img" aria-label="Photo of a fender being worked on" style="background:linear-gradient(160deg,#7b8187,#2b3035)"><b>Fender</b><i>Repair</i></div>
</div>
<div class="abs chev chev-line" style="left:143px;top:915px;border:none"><svg width="8" height="12" viewBox="0 0 8 12"><path d="M6.5 1 1.5 6l5 5" fill="none" stroke="var(--blue)" stroke-width="2"/></svg></div>
<div class="abs chev chev-solid" style="left:1030px;top:915px"><svg width="8" height="12" viewBox="0 0 8 12"><path d="M1.5 1l5 5-5 5" fill="none" stroke="#fff" stroke-width="2"/></svg></div>

<!-- process -->
<div class="abs sec-title" style="top:1080px">Repair Process</div>
<div class="abs lead" style="top:1116px;font-size:13.5px;line-height:18px;color:#555">The BrookVale seven-step repair process ensures your vehicle is inspected and repaired only by industry-certified<br>technicians, whose priority is getting you back on the road safely.</div>
<div class="abs rule" style="left:207px;top:1171px;width:785px"></div>
<div class="abs notch" style="left:591px;top:1162px;background:var(--white)"></div>

<div class="abs chev chev-line" style="left:143px;top:1291px"><svg width="8" height="12" viewBox="0 0 8 12"><path d="M6.5 1 1.5 6l5 5" fill="none" stroke="var(--blue)" stroke-width="2"/></svg></div>
<div class="abs chev chev-line" style="left:1031px;top:1291px"><svg width="8" height="12" viewBox="0 0 8 12"><path d="M1.5 1l5 5-5 5" fill="none" stroke="var(--blue)" stroke-width="2"/></svg></div>

<div class="abs step" style="left:208px;top:1212px"><svg width="42" height="40" viewBox="0 0 42 40"><rect x="3" y="2" width="36" height="36" fill="none" stroke="var(--blue)" stroke-width="3"/><rect x="3" y="8" width="36" height="2" fill="var(--blue)"/><rect x="9" y="20" width="24" height="12" rx="3" fill="var(--blue)"/><rect x="12" y="15" width="18" height="6" fill="var(--blue)"/></svg><span>Vehicle Drop Off</span></div>
<div class="abs step on" style="left:419px;top:1212px"><svg width="58" height="30" viewBox="0 0 58 30"><path d="M6 16 14 8h26l8 8h4v7H4v-7z" fill="#fff"/><circle cx="15" cy="23" r="4" fill="var(--blue)" stroke="#fff" stroke-width="2"/><circle cx="43" cy="23" r="4" fill="var(--blue)" stroke="#fff" stroke-width="2"/><rect x="27" y="23" width="4" height="7" fill="#fff"/></svg><span style="margin-top:24px">Body Repair</span></div>
<div class="abs step" style="left:629px;top:1212px"><svg width="40" height="48" viewBox="0 0 40 48" style="margin-top:24px"><rect x="18" y="2" width="8" height="14" rx="2" fill="var(--blue)"/><path d="M14 16h16l-2 10h-12z" fill="var(--blue)"/><rect x="19" y="26" width="6" height="18" fill="var(--blue)"/><circle cx="6" cy="22" r="1.5" fill="var(--blue)"/><circle cx="9" cy="18" r="1.5" fill="var(--blue)"/><circle cx="4" cy="27" r="1.5" fill="var(--blue)"/></svg><span style="margin-top:8px">Painting / Polish</span></div>
<div class="abs step" style="left:840px;top:1212px"><svg width="44" height="44" viewBox="0 0 44 44" style="margin-top:28px"><circle cx="22" cy="22" r="19" fill="none" stroke="var(--blue)" stroke-width="5"/><circle cx="22" cy="22" r="5" fill="var(--blue)"/><path d="M22 6v10M22 28v10M6 22h10M28 22h10M11 11l7 7M26 26l7 7M33 11l-7 7M18 26l-7 7" stroke="var(--blue)" stroke-width="3"/></svg><span style="margin-top:8px">Reassembly</span></div>

<div class="abs step-head">Body Repair</div>
<div class="abs step-text">After your vehicle is evaluated, it moves into the body shop, where we remove all parts requiring separate repair or replacement, and perform body and structural repair work. Meanwhile, all repair work undergoes a rigorous quality control inspection.</div>
<div class="abs learn">Learn More »</div>

<!-- features -->
<div class="abs features-photo" role="img" aria-label="Photo of a smiling technician in a blue work uniform"></div>
<div class="abs features-bg" role="img" aria-label="Faded photo of an engine bay"></div>
<div class="abs menu">
  <div class="menu-row"><div class="ic"><svg width="32" height="22" viewBox="0 0 32 22"><path d="M3 12 7 5h12l4 7v6H3z" fill="none" stroke="#fff" stroke-width="2"/><circle cx="23" cy="13" r="6" fill="var(--green)" stroke="#fff" stroke-width="2"/><path d="M27 17l4 4" stroke="#fff" stroke-width="2"/></svg></div><span class="lbl">All Makes &amp; Models</span></div>
  <div class="menu-row on"><div class="ic"><svg width="22" height="26" viewBox="0 0 22 26"><circle cx="11" cy="10" r="8" fill="none" stroke="#fff" stroke-width="2"/><path d="M7 10l3 3 5-6" fill="none" stroke="#fff" stroke-width="2"/><path d="M6 17l-3 8 4-2 3 3M16 17l3 8-4-2-3 3" fill="none" stroke="#fff" stroke-width="1.6"/></svg></div><span class="lbl">Lifetime Warranty</span></div>
  <div class="menu-row"><div class="ic"><svg width="22" height="24" viewBox="0 0 22 24"><path d="M11 1 2 4v7c0 6 4 10 9 12 5-2 9-6 9-12V4z" fill="#fff"/><path d="M7 12l3 3 5-6" fill="none" stroke="var(--green)" stroke-width="2"/></svg></div><span class="lbl">Quality Control</span></div>
  <div class="menu-row"><div class="ic"><svg width="18" height="24" viewBox="0 0 18 24"><rect x="1" y="1" width="16" height="22" fill="none" stroke="#fff" stroke-width="2"/><rect x="4" y="4" width="10" height="4" fill="#fff"/><path d="M4 12h2M8 12h2M12 12h2M4 16h2M8 16h2M12 16h2M4 20h2M8 20h2M12 20h2" stroke="#fff" stroke-width="2"/></svg></div><span class="lbl">Free Estimates</span></div>
  <div class="menu-row"><div class="ic"><svg width="32" height="22" viewBox="0 0 32 22"><path d="M2 13 6 5h12l4 8v5H2z" fill="none" stroke="#fff" stroke-width="2"/><circle cx="24" cy="13" r="6" fill="var(--green)" stroke="#fff" stroke-width="2"/><path d="M24 10v3h3" stroke="#fff" stroke-width="2" fill="none"/></svg></div><span class="lbl">Car Rentals &amp; Towing</span></div>
  <div class="menu-row"><div class="ic"><svg width="24" height="24" viewBox="0 0 24 24"><circle cx="12" cy="12" r="7" fill="none" stroke="#fff" stroke-width="3" stroke-dasharray="4 2"/><circle cx="12" cy="12" r="3" fill="#fff"/></svg></div><span class="lbl">Insurance Partners</span></div>
  <div class="menu-row"><div class="ic"><svg width="30" height="22" viewBox="0 0 30 22"><rect x="1" y="1" width="28" height="20" fill="none" stroke="#fff" stroke-width="2"/><rect x="5" y="5" width="20" height="12" fill="none" stroke="#fff" stroke-width="1.5"/><circle cx="15" cy="10" r="3" fill="none" stroke="#fff" stroke-width="1.5"/></svg></div><span class="lbl">Dealer Certified</span></div>
  <div class="menu-row" style="border-bottom:none"><div class="ic"><svg width="32" height="22" viewBox="0 0 32 22"><rect x="1" y="3" width="24" height="16" rx="2" fill="none" stroke="#fff" stroke-width="2"/><rect x="1" y="7" width="24" height="3" fill="#fff"/><circle cx="25" cy="15" r="5" fill="var(--green)" stroke="#fff" stroke-width="2"/></svg></div><span class="lbl">Payment Options</span></div>
</div>
<div class="abs panel-title">Lifetime Warranty</div>
<div class="abs panel-text">At BrookVale, we proudly stand by the quality of our work.<br>That’s why every repair performed at each of our locations nationwide is backed<br>by the BrookVale lifetime warranty. In the rare instance that<br>you’re not 100 percent satisfied with the quality of your repair, simply<br>return your vehicle to any location and our team will work to make<br>it right. Guaranteed.</div>
<div class="abs panel-link">Read More »</div>
<div class="abs rule" style="left:552px;top:1939px;width:416px"></div>
<div class="abs contact-h">Contact Us</div>
<div class="abs contact-n">555.014.2290</div>

<!-- testimonials -->
<div class="abs sec-title" style="top:2122px">What Our Customer Says?</div>
<div class="abs rule" style="left:207px;top:2177px;width:785px"></div>
<div class="abs notch" style="left:591px;top:2168px;background:var(--white)"></div>
<div class="abs chev chev-line" style="left:143px;top:2377px"><svg width="8" height="12" viewBox="0 0 8 12"><path d="M6.5 1 1.5 6l5 5" fill="none" stroke="var(--blue)" stroke-width="2"/></svg></div>
<div class="abs chev chev-line" style="left:1031px;top:2377px"><svg width="8" height="12" viewBox="0 0 8 12"><path d="M1.5 1l5 5-5 5" fill="none" stroke="var(--blue)" stroke-width="2"/></svg></div>

<div class="abs quote-card quote-dark" role="img" aria-label="Photo of a customer in a suit, darkened behind the review"></div>
<div class="abs qmark" style="left:232px;top:2244px">“</div>
<div class="abs qtext" style="left:260px;top:2268px;width:262px;color:#fff">Outstanding customer focus &amp; service Greeted professionally by Dana and staff Guided me thru the process all the way thru Kept in constant communication (text, phone) on repair status Promised and delivered on job completion Excellent pick-up and discharge/ paperwork process ...</div>
<div class="abs qname" style="left:260px;top:2436px;color:#fff">Calvin R</div>
<div class="abs qloc" style="left:260px;top:2462px;color:#fff">FL - 2210 Harbor Pike,<br>Eastport.</div>
<div class="abs submit">— SUBMIT YOUR REVIEWS —</div>

<div class="abs qmark" style="left:660px;top:2244px">“</div>
<div class="abs qtext" style="left:688px;top:2268px;width:262px;color:var(--muted)">WOW! This is the first time that I have used Pondly. I highly "wreck-ommend" this facility to anyone who lives in the Valparaiso, In area. The staff's first priority is to their customer! Pleasant, professional, respectful and diligent are a few adjectives that I'd use to describe the service that I received ...</div>
<div class="abs qname" style="left:688px;top:2436px;color:var(--ink)">Tessa W</div>
<div class="abs qloc" style="left:688px;top:2462px;color:#8a8d90">FL - 418 W Alder St,<br>Millbrook</div>
<div class="abs" style="left:635px;top:2551px;width:357px;height:4px;background:var(--green)"></div>

<!-- offers -->
<div class="abs offers-bg"></div>
<svg class="abs" style="left:0;top:2604px" width="663" height="232" viewBox="0 0 663 232"><polygon points="0,0 663,0 537,232 0,232" fill="var(--blue)"/></svg>
<div class="abs offers-h" style="left:156px;top:2640px;color:#fff">Pondly Offers!</div>
<div class="abs" style="left:156px;top:2677px;width:420px;font-size:13.5px;line-height:18px;color:#fff">Valuable savings and special offers on our repair services.<br>Take advantage of these offers exclusively available at Pondly<br>Collision &amp; Glass.</div>
<div class="abs btn btn-green" style="left:156px;top:2762px;width:152px;height:32px">— VIEW OFFERS —</div>
<div class="abs offers-h" style="left:688px;top:2640px;color:var(--blue)">Find a Center Near You</div>
<div class="abs search"><svg width="14" height="14" viewBox="0 0 14 14"><circle cx="7" cy="7" r="5.5" fill="none" stroke="#b5b8bb" stroke-width="1.4"/><circle cx="7" cy="7" r="1.8" fill="#b5b8bb"/></svg>Enter an Add., City and State or Zip<svg style="margin-left:auto" width="20" height="20" viewBox="0 0 20 20"><circle cx="8" cy="8" r="6.5" fill="none" stroke="var(--blue)" stroke-width="2"/><path d="M13 13l6 6" stroke="var(--blue)" stroke-width="2"/></svg></div>
<div class="abs" style="left:688px;top:2746px;font-size:13.5px;color:var(--ink)">We’re here to help in case of an emergency, Call Us</div>
<div class="abs" style="left:688px;top:2766px;font-size:24px;color:var(--ink)">555.014.2290</div>

<!-- footer -->
<div class="abs footer"></div>
<div class="abs f-title" style="left:156px;top:2878px;font-size:19px"><b>BrookVale</b> Collision Repair</div>
<div class="abs" style="left:156px;top:2916px;width:290px;font-size:12.5px;line-height:17.6px;color:#d4d6d8">Fix Right, the first time, every time.<br>BrookVale, The trusted pick in collision repair.</div>
<div class="abs" style="left:156px;top:2983px;font-size:13px;color:#e4e6e8">Get Social:</div>
<div class="abs social" style="left:156px;top:3012px"><span></span><span class="on"></span><span></span><span></span></div>
<div class="abs" style="left:156px;top:3066px;font-size:11px;line-height:16px;color:#c4c6c8">© 2016 BrookVale Collision Repair,<br>All rights reserved.</div>

<div class="abs f-title" style="left:512px;top:2878px">Quick Link</div>
<ul class="abs f-list" style="left:512px;top:2914px">
  <li>Home</li><li class="on">Company</li><li>Repair Services</li><li>Our Process</li><li>Careers</li><li>Customer Review</li><li>Feedback</li><li>Location</li><li>Contact</li>
</ul>
<ul class="abs f-list" style="left:664px;top:2914px">
  <li>Legal</li><li>Acquisitions</li><li>Gurantee</li><li>Agent</li><li>Privacy Policy</li><li>Terms of Use</li><li>Sitemap</li><li>FAQ</li>
</ul>

<div class="abs f-title" style="left:840px;top:2878px">Locations</div>
<div class="abs" style="left:839px;top:2914px;font-size:13px;line-height:17px;color:#d4d6d8">7720 Quarry Lane<br>Fenwick Street<br>KY 40811</div>
<div class="abs" style="left:839px;top:2984px;font-size:13px;line-height:17px;color:#d4d6d8">Phone:<br>555.014.2290</div>
<div class="abs" style="left:839px;top:3036px;font-size:13px;line-height:17px;color:#d4d6d8">Email:<br>support@brookvale.example</div>
<svg class="abs" style="left:1092px;top:2882px" width="26" height="30" viewBox="0 0 26 30"><path d="M13 2 2 13h7v15h8V13h7z" fill="none" stroke="#8a8d91" stroke-width="2.4" stroke-linejoin="round"/></svg>

</body>
</html>
```